Bildmarkt Speech for a trade show in Las Vegas

I've tried to create the powerpoint on my own. I used a template, but am not satisfied with the look and feel. I'd like something more professional looking. I need this powerpoint for an upcoming speech. I need the ppt to be in a format in which I can edit it for last-minute changes before my speech.

The Power Point has a lot of slides, but mostly I'm looking for a few good backgrounds so that every slide doesn't have to be completely unique. Plus, if you can clean up some of my graphics, that would be great too. Feel free to message me with any questions. Happy to help out.

Target Market(s)

Leaders in Construction and Manufacturing

Industry/Entity Type

Construction

Font styles to use
Sans Serif

Colors

Designer to choose colors to be used in the design.

Requirements
Must have
• The ability for me to edit the slides so that I can do some last-minute changes.
• I need to have the Bildmarkt/TerraMix logo (small round logo) on the bottom of each slide (or at least most of them).
Nice to have
• Pictures of people on construction sites using heavy equipment. (Backhoes, Loaders, Grubbers, Trench Owl products, Ironmoth products, Paul Haskin products, etc)

```html
<!DOCTYPE html>
<html lang="en">
<head>
<meta charset="utf-8">
<title>Becoming a Construction Leader Worth Following – Slide Masters</title>
<link href="https://fonts.googleapis.com/css2?family=Ubuntu:wght@400;500;700&family=Open+Sans:ital,wght@0,400;0,600;0,700;1,400&display=swap" rel="stylesheet">
<style>
:root{
  --red:#b0272d;
  --red-soft:#d9434e;
  --pink:#ec8593;
  --blue:#0f3a8c;
  --navy:#14307a;
  --orange:#e8921d;
  --yellow:#f5b31a;
  --green:#1a8f3a;
  --ink:#111;
  --grey:#6b6b6b;
  --paper:#f4f4f4;
  --canvas:#f6f6f6;
}
*{box-sizing:border-box;margin:0;padding:0}
html,body{width:1028px;height:1200px;overflow:hidden;background:var(--canvas)}
body{position:relative;font-family:"Open Sans",Arial,sans-serif;color:var(--ink)}
.slide{position:absolute;width:299px;height:168px;background:var(--paper);overflow:hidden;box-shadow:0 6px 10px rgba(0,0,0,.28)}
.h{font-family:"Ubuntu",Arial,sans-serif;font-weight:700;text-transform:uppercase}
.photo{position:absolute}
.dots{position:absolute;display:flex;gap:3px}
.dots i{width:3px;height:3px;border-radius:50%;background:var(--green);display:block}
.mark{position:absolute;right:5px;bottom:6px;display:flex;align-items:center;gap:2px;font-family:"Ubuntu",sans-serif;font-weight:700;font-size:5px;color:var(--blue)}
.mark b{width:9px;height:9px;border-radius:50%;background:var(--orange);display:block}
.bar-head{position:absolute;left:0;right:0;top:7px;height:22px;border-top:2px solid var(--yellow);color:#fff;font-size:9.5px;padding:5px 11px;letter-spacing:.2px}
.bar-head.red{background:var(--red)}
.bar-head.blue{background:var(--blue)}
.foot-line{position:absolute;left:0;right:0;bottom:0;height:2px}
.sub{position:absolute;left:11px;top:31px;font-family:"Ubuntu",sans-serif;font-weight:700;font-size:5.5px;color:var(--red);letter-spacing:.6px}
.wash{position:absolute;inset:0;background:linear-gradient(120deg,#efefef,#e2e2e2 60%,#ececec)}

/* hero */
.hero{left:359px;top:24px;width:633px;height:357px;background:#fff}
.hero .photo{left:0;top:0;width:633px;height:222px;background:linear-gradient(180deg,#b9c3cb 0%,#a9a59b 45%,#b49a72 70%,#8f7e63 100%)}
.hero .t1{position:absolute;left:55px;top:205px;font-size:29px}
.hero .t2{position:absolute;left:53px;top:234px;font-size:45px;color:var(--red);letter-spacing:.5px}
.hero .t3{position:absolute;right:53px;top:283px;font-size:30px}
.hero .rule{position:absolute;left:0;right:0;bottom:0;height:5px;background:var(--yellow)}

/* welcome */
.welcome{left:31px;top:24px}
.welcome .stripe{position:absolute;left:0;top:0;bottom:0;width:5px;background:linear-gradient(var(--red),var(--red) 70%,var(--yellow))}
.welcome .photo{left:100px;top:20px;right:0;bottom:0;background:radial-gradient(ellipse at 40% 70%,#cfcfcf,#e8e8e8 70%)}
.welcome .t{position:absolute;left:23px;top:30px;font-size:21px}
.welcome .seal{position:absolute;left:160px;top:50px;display:flex;align-items:center;gap:5px;font-family:"Ubuntu",sans-serif;font-weight:700;font-size:9px;color:var(--blue);white-space:nowrap}
.welcome .seal b{width:30px;height:30px;border-radius:50%;background:var(--orange);display:block;flex:none}
.welcome .url{position:absolute;left:26px;bottom:6px;font-size:4.5px;letter-spacing:2px;color:#555}

/* master title */
.master{left:31px;top:213px}
.master .photo{inset:0;background:linear-gradient(135deg,#d9d4cb,#e8e4dc 50%,#d2c7b5)}
.master .a{position:absolute;left:20px;top:40px;font-size:14px}
.master .b{position:absolute;left:19px;top:55px;font-size:21px;color:var(--red)}
.master .c{position:absolute;right:31px;top:77px;font-size:14px}
.master .d{position:absolute;left:21px;top:140px;font-family:"Ubuntu",sans-serif;font-weight:500;font-size:8.5px;color:#444}
.master .e{position:absolute;left:21px;top:152px;font-size:5px;color:#666}
.master .mark{bottom:10px;right:8px;font-size:6px}
.master .mark b{width:14px;height:14px}

/* investment */
.invest{left:31px;top:401px}
.invest .photo{inset:0;background:linear-gradient(180deg,#e6e6e6,#d5d5d5)}
.invest .frame{position:absolute;left:10px;top:8px;right:10px;bottom:8px;border:1px solid var(--orange)}
.invest .band{position:absolute;left:0;right:0;top:53px;height:61px;background:linear-gradient(90deg,var(--red) 0%,#c2372a 50%,var(--orange) 100%)}
.invest .your{position:absolute;left:36px;top:80px;color:#fff;font-size:15px}
.invest .ninety{position:absolute;left:76px;top:53px;color:#fff;font-family:"Ubuntu",sans-serif;font-weight:700;font-size:55px;letter-spacing:-2px}
.invest .min{position:absolute;left:137px;top:70px;color:#fff;font-size:8.5px}
.invest .inv{position:absolute;left:140px;top:81px;color:#fff;font-size:15px}

/* start stop */
.startstop{left:364px;top:401px;background:#fff}
.startstop .title{position:absolute;left:0;right:0;top:38px;text-align:center;font-size:12px;color:var(--blue)}
.startstop .title span{color:var(--red)}
.startstop .block{position:absolute;left:0;right:0;top:58px;height:79px;background:var(--blue)}
.startstop .block::before{content:"";position:absolute;left:8px;top:0;bottom:0;width:4px;background:#fff}
.startstop .q{position:absolute;left:26px;right:18px;top:86px;text-align:center;color:#fff;font-size:9px;line-height:1.3;font-weight:300}
.startstop .mk{position:absolute;left:24px;top:60px;color:#2a4a8e;font-size:34px;font-family:Georgia,serif;font-weight:700}

/* life effect */
.life{left:692px;top:401px}

/* mentor */
.mentor{left:31px;top:589px}
.mentor .txt{position:absolute;left:11px;top:36px;font-size:7.5px;font-weight:700;line-height:1.2;width:115px}
.mentor .txt2{position:absolute;left:11px;top:70px;font-size:8px;line-height:1.2;width:60px}
.mentor .lbl{position:absolute;font-size:5px;color:#fff;white-space:nowrap}
.mentor .center{position:absolute;left:152px;top:86px;width:72px;text-align:center;font-family:"Ubuntu",sans-serif;font-weight:500;font-size:9px;line-height:1.3}

/* disciplines icons */
.disc-icons{left:364px;top:589px}
.disc-icons .item{position:absolute;display:flex;align-items:center;gap:6px;font-family:"Ubuntu",sans-serif;font-weight:700;font-size:7px;line-height:1.2}
.disc-icons .item .sep{width:1px;height:26px;background:#222}
.disc-icons .item.r{color:var(--red)}
.disc-icons .item.r .sep{background:var(--red)}

/* disciplines numbers */
.disc-nums{left:692px;top:589px}
.disc-nums .tile{position:absolute;width:114px;height:32px;background:var(--red);border-radius:3px;box-shadow:0 3px 4px rgba(0,0,0,.3);display:flex;align-items:center;color:#fff}
.disc-nums .n{font-family:"Ubuntu",sans-serif;font-weight:500;font-size:22px;padding:0 5px 0 5px;border-right:1px solid #fff;line-height:24px}
.disc-nums .l{font-family:"Ubuntu",sans-serif;font-weight:500;font-size:6.8px;padding-left:5px;line-height:1.1}

/* capacity cover */
.cap{left:31px;top:778px}
.cap .photo{inset:0;background:linear-gradient(180deg,#cfc5a7,#b4a98d 50%,#a3a6b6)}
.cap .frame{position:absolute;left:5px;top:5px;right:5px;bottom:5px;border:1px solid rgba(255,255,255,.8)}
.cap .band{position:absolute;left:125px;right:0;top:54px;height:51px;background:linear-gradient(90deg,var(--red) 0%,#c2412b 55%,var(--orange) 100%);border-radius:8px 0 0 8px}
.cap .n{position:absolute;left:140px;top:60px;color:#fff;font-family:"Ubuntu",sans-serif;font-weight:500;font-size:30px}
.cap .sep{position:absolute;left:182px;top:62px;width:1px;height:34px;background:#fff}
.cap .l{position:absolute;left:193px;top:69px;color:#fff;font-size:10px;line-height:1.1}

/* management */
.mgmt{left:364px;top:778px}
.mgmt .block{position:absolute;left:6px;top:43px;width:59px;height:107px;background:var(--blue)}
.mgmt .block::before{content:"";position:absolute;left:-6px;top:0;bottom:0;width:3px;background:var(--blue)}
.mgmt .cost{position:absolute;left:11px;top:86px;color:#fff;font-family:"Ubuntu",sans-serif;font-weight:500;font-size:12px}
.mgmt .q{position:absolute;left:80px;top:53px;font-size:7px;font-weight:700}
.mgmt .b{position:absolute;left:80px;font-size:6.5px;font-style:italic;line-height:1.75;width:205px;padding-left:8px}
.mgmt .b::before{content:"";position:absolute;left:0;top:4px;width:3px;height:3px;border-radius:50%;background:var(--blue)}

/* capacity monkeys */
.monkeys{left:692px;top:778px}
.monkeys .photo{left:24px;top:55px;width:75px;height:85px;background:linear-gradient(150deg,#8d7a5e,#c9b79a 55%,#6c5e4b)}
.monkeys .q{position:absolute;left:134px;top:60px;font-size:7px;font-weight:700;line-height:1.2}
.monkeys .b{position:absolute;left:134px;font-size:6.5px;font-style:italic;padding-left:7px}
.monkeys .b::before{content:"";position:absolute;left:0;top:3px;width:3px;height:3px;border-radius:50%;background:var(--red)}

/* matrix */
.matrix{left:31px;top:966px;background:#f7f7f7}
.matrix .side{position:absolute;left:0;top:0;bottom:0;width:27px;background:var(--blue)}
.matrix .side span{position:absolute;left:50%;top:50%;transform:translate(-50%,-50%) rotate(-90deg);white-space:nowrap;color:#fff;font-size:9.5px}
.matrix .ax{position:absolute;font-size:7px;color:var(--red);text-align:center;line-height:1.1}
.matrix .q{position:absolute;width:67px;height:34px;border:1px dashed #999;text-align:center;padding-top:7px;font-family:"Ubuntu",sans-serif;font-weight:500;font-size:7.5px;color:var(--blue);line-height:1.2}
.matrix .q small{display:block;font-family:"Open Sans",sans-serif;font-weight:400;font-size:5px}

/* magic circle */
.magic{left:364px;top:966px}
.magic .credit{position:absolute;left:11px;bottom:7px;font-size:3.5px;color:var(--red)}

/* driving culture */
.culture{left:692px;top:966px}
.culture .photo{inset:0;background:linear-gradient(180deg,#8a9c6d 0%,#a89b7e 50%,#7f6d55 100%)}
.culture .panel{position:absolute;left:24px;top:0;bottom:0;width:111px;background:rgba(20,58,140,.92)}
.culture .t{position:absolute;left:41px;top:14px;color:#fff;font-size:17px;line-height:1.27}
.culture .dots{left:43px;top:99px}
.culture .dots i{background:#fff}
.culture .mark{top:8px;bottom:auto;right:8px;color:#fff;font-size:6px}
.culture .mark b{width:14px;height:14px}

.caption{position:absolute;left:0;right:0;top:1162px;text-align:center;font-size:14.5px;color:#222}
</style>
</head>
<body>

<!-- Welcome -->
<section class="slide welcome">
  <div class="photo" role="img" aria-label="Faded photo of a wheel loader and silos"></div>
  <div class="stripe"></div>
  <h1 class="t h">Welcome</h1>
  <div class="dots" style="left:26px;top:54px"><i></i><i></i><i></i></div>
  <div class="seal"><b></b>Bildmarkt/TerraMix</div>
  <div class="url">WWW.BILDMARKTTERRAMIX.COM</div>
</section>

<!-- Master title -->
<section class="slide master">
  <div class="photo" role="img" aria-label="Faded aerial photo of a quarry with a loader"></div>
  <div class="dots" style="left:21px;top:33px"><i></i><i></i><i></i></div>
  <div class="a h">Becoming a</div>
  <div class="b h">Construction Leader</div>
  <div class="c h">Worth Following</div>
  <div class="d h">Master Slides Presentation</div>
  <div class="e">Easy editable Master slides includes</div>
  <div class="mark"><b></b>Bildmarkt</div>
</section>

<!-- Hero -->
<section class="slide hero">
  <div class="photo" role="img" aria-label="Photo of a yellow wheel loader tipping gravel into a dump truck beside silos"></div>
  <div class="dots" style="left:58px;top:191px"><i style="width:7px;height:7px"></i><i style="width:7px;height:7px"></i><i style="width:7px;height:7px"></i></div>
  <div class="t1 h">Becoming a</div>
  <div class="t2 h">Construction Leader</div>
  <div class="t3 h">Worth Following</div>
  <div class="rule"></div>
</section>

<!-- 90 minute -->
<section class="slide invest">
  <div class="photo" role="img" aria-label="Faded photo of a loader at a quarry"></div>
  <div class="frame"></div>
  <div class="band"></div>
  <div class="dots" style="left:145px;top:46px"><i></i><i></i><i></i></div>
  <div class="your h">Your</div>
  <div class="ninety">90</div>
  <div class="min h">-Minute</div>
  <div class="inv h">Investment</div>
</section>

<!-- Starting & stopping -->
<section class="slide startstop">
  <div class="dots" style="left:143px;top:31px"><i></i><i></i><i></i></div>
  <div class="title h">Starting &amp; <span>Stopping</span></div>
  <div class="block"></div>
  <div class="mk">“</div>
  <p class="q">In light of what you’ve just heard, what are some things you need to either STOP or START doing?</p>
</section>

<!-- Life effect -->
<section class="slide life">
  <div class="wash"></div>
  <div class="bar-head red h">Leaders Worth Following</div>
  <div class="sub">THE LIFE EFFECT</div>
  <svg width="299" height="168" style="position:absolute;left:0;top:0">
    <defs><marker id="ah" markerWidth="6" markerHeight="6" refX="5" refY="3" orient="auto"><path d="M0,0 L6,3 L0,6z" fill="#000"/></marker>
    <marker id="ab" markerWidth="5" markerHeight="5" refX="4" refY="2.5" orient="auto"><path d="M0,0 L5,2.5 L0,5z" fill="#1a2fd0"/></marker>
    <marker id="ag" markerWidth="5" markerHeight="5" refX="4" refY="2.5" orient="auto"><path d="M0,0 L5,2.5 L0,5z" fill="#1ea53a"/></marker></defs>
    <line x1="87" y1="149" x2="87" y2="42" stroke="#000" stroke-width="1" marker-end="url(#ah)"/>
    <line x1="87" y1="149" x2="236" y2="149" stroke="#000" stroke-width="1" marker-end="url(#ah)"/>
    <line x1="88" y1="148" x2="223" y2="45" stroke="#1ea53a" stroke-width="1.2" marker-end="url(#ag)"/>
    <line x1="87" y1="95" x2="232" y2="95" stroke="#000" stroke-width=".7"/>
    <g stroke="#1a2fd0" stroke-width="1">
      <line x1="93" y1="143" x2="93" y2="97" marker-end="url(#ab)"/>
      <line x1="100" y1="138" x2="100" y2="97" marker-end="url(#ab)"/>
      <line x1="107" y1="132" x2="107" y2="97" marker-end="url(#ab)"/>
      <line x1="114" y1="127" x2="114" y2="97" marker-end="url(#ab)"/>
      <line x1="121" y1="122" x2="121" y2="97" marker-end="url(#ab)"/>
      <line x1="128" y1="116" x2="128" y2="97" marker-end="url(#ab)"/>
      <line x1="135" y1="111" x2="135" y2="97" marker-end="url(#ab)"/>
    </g>
    <text x="176" y="102" font-size="5" font-family="Open Sans" font-weight="600">Your Leadership Skills</text>
    <text x="165" y="84" font-size="5.5" fill="#1ea53a" font-family="Open Sans" transform="rotate(-37 165 84)">Size of your organization</text>
  </svg>
  <div class="mark"><b></b>Bildmarkt</div>
  <div class="foot-line" style="background:var(--red)"></div>
</section>

<!-- What to mentor -->
<section class="slide mentor">
  <div class="wash"></div>
  <div class="bar-head blue h">What to Mentor?</div>
  <p class="txt">Employees just doing their job will not get them a pay raise or a promotion.</p>
  <p class="txt2"><b>How</b> they do their job <b>will.</b></p>
  <svg width="299" height="168" style="position:absolute;left:0;top:0">
    <g transform="translate(188 95) scale(1.58 1) rotate(-90)" fill="none" stroke-width="23">
      <circle r="49" stroke="#b0272d" stroke-dasharray="33 275" stroke-dashoffset="0"/>
      <circle r="49" stroke="#c8323b" stroke-dasharray="33 275" stroke-dashoffset="-34.2"/>
      <circle r="49" stroke="#d9434e" stroke-dasharray="33 275" stroke-dashoffset="-68.4"/>
      <circle r="49" stroke="#ec8593" stroke-dasharray="33 275" stroke-dashoffset="-102.6"/>
      <circle r="49" stroke="#9c9c9c" stroke-dasharray="33 275" stroke-dashoffset="-136.8"/>
      <circle r="49" stroke="#8a8a8a" stroke-dasharray="33 275" stroke-dashoffset="-171"/>
      <circle r="49" stroke="#7a7a7a" stroke-dasharray="33 275" stroke-dashoffset="-205.2"/>
      <circle r="49" stroke="#6a6a6a" stroke-dasharray="33 275" stroke-dashoffset="-239.4"/>
      <circle r="49" stroke="#585858" stroke-dasharray="33 275" stroke-dashoffset="-273.6"/>
    </g>
  </svg>
  <span class="lbl" style="left:195px;top:51px">Collaboration</span>
  <span class="lbl" style="left:241px;top:72px">Driver</span>
  <span class="lbl" style="left:250px;top:103px">No Rumors</span>
  <span class="lbl" style="left:222px;top:133px">Low Stress</span>
  <span class="lbl" style="left:171px;top:143px">Appreciative</span>
  <span class="lbl" style="left:122px;top:131px">Thinking Ahead</span>
  <span class="lbl" style="left:104px;top:97px;line-height:1.1">Actively<br>Engaged</span>
  <span class="lbl" style="left:111px;top:73px">No Whining</span>
  <span class="lbl" style="left:150px;top:52px">Teamwork</span>
  <div class="center">YOU DOING<br>YOUR JOB.</div>
  <div class="mark"><b></b>Bildmarkt</div>
  <div class="foot-line" style="background:var(--blue)"></div>
</section>

<!-- Four disciplines icons -->
<section class="slide disc-icons">
  <div class="wash"></div>
  <div class="bar-head red h">The Four Disciplines</div>
  <div class="item" style="left:26px;top:59px">
    <svg width="20" height="20" viewBox="0 0 20 20" fill="none" stroke="#222" stroke-width="1"><rect x="2" y="12" width="4" height="6"/><rect x="8" y="8" width="4" height="10"/><rect x="14" y="4" width="4" height="14"/><path d="M2 9 L9 4 L13 6 L18 1"/></svg>
    <span class="sep"></span><span>INCREASING<br>YOUR CAPACITY</span>
  </div>
  <div class="item" style="left:162px;top:59px">
    <svg width="22" height="22" viewBox="0 0 22 22" fill="none" stroke="#222" stroke-width="1"><circle cx="11" cy="11" r="10"/><circle cx="11" cy="11" r="7.5"/><path d="M15 7 L12 12 L7 15 L10 10 Z"/></svg>
    <span class="sep"></span><span>DRIVING THE<br>RIGHT CULTURE</span>
  </div>
  <div class="item r" style="left:26px;top:114px">
    <svg width="22" height="20" viewBox="0 0 22 20" fill="none" stroke="#b0272d" stroke-width="1"><circle cx="11" cy="3" r="2"/><path d="M8 9 Q11 5 14 9"/><circle cx="4" cy="12" r="2"/><path d="M1 18 Q4 14 7 18"/><circle cx="18" cy="12" r="2"/><path d="M15 18 Q18 14 21 18"/><path d="M11 10 V12 M4 12 H18"/></svg>
    <span class="sep"></span><span>YOUR EMPLOYEES’<br>LEADERSHIP STYLE</span>
  </div>
  <div class="item" style="left:162px;top:114px">
    <svg width="22" height="18" viewBox="0 0 22 18" fill="none" stroke="#222" stroke-width="1"><path d="M1 5 L6 3 L11 6 L16 3 L21 5"/><path d="M5 7 L11 13 L17 7"/><path d="M8 10 L10 12 M11 9 L13 11"/></svg>
    <span class="sep"></span><span>BEING<br>A TRUST DRIVER</span>
  </div>
  <div class="mark"><b></b>Bildmarkt</div>
  <div class="foot-line" style="background:var(--red)"></div>
</section>

<!-- Four disciplines numbers -->
<section class="slide disc-nums">
  <div class="wash"></div>
  <div class="bar-head blue h">The Four Disciplines</div>
  <div class="tile" style="left:25px;top:54px"><span class="n">01</span><span class="l">INCREASING<br>YOUR CAPACITY</span></div>
  <div class="tile" style="left:158px;top:54px"><span class="n">02</span><span class="l">DRIVING THE<br>RIGHT CULTURE</span></div>
  <div class="tile" style="left:25px;top:109px"><span class="n">03</span><span class="l">YOUR EMPLOYEES’<br>LEADERSHIP STYLE</span></div>
  <div class="tile" style="left:158px;top:109px"><span class="n">04</span><span class="l">BEING<br>A TRUST DRIVER</span></div>
  <div class="mark"><b></b>Bildmarkt</div>
  <div class="foot-line" style="background:var(--blue)"></div>
</section>

<!-- Increasing capacity cover -->
<section class="slide cap">
  <div class="photo" role="img" aria-label="Photo of a yellow crawler dozer at a work site"></div>
  <div class="frame"></div>
  <div class="band"></div>
  <div class="n">01</div>
  <div class="sep"></div>
  <div class="l h">Increasing<br>Your Capacity</div>
</section>

<!-- Management ready -->
<section class="slide mgmt">
  <div class="wash"></div>
  <div class="bar-head blue h">Management Ready</div>
  <div class="block"></div>
  <div class="cost">1.Cost ?</div>
  <p class="q">Will their request cost money?</p>
  <div class="dots" style="left:81px;top:64px"><i></i><i></i><i></i></div>
  <p class="b" style="top:74px">If so, they should know if it fits within the budget.</p>
  <p class="b" style="top:95px">If not, can they justify going over budget, or can they suggest other things within the budget we can scaled back or eliminate in order to offset the cost?</p>
  <div class="mark"><b></b>Bildmarkt</div>
  <div class="foot-line" style="background:var(--blue)"></div>
</section>

<!-- Discipline your capacity -->
<section class="slide monkeys">
  <div class="wash"></div>
  <div class="bar-head red h">Discipline:&nbsp; Your Capacity</div>
  <div class="sub">THE LIFE EFFECT</div>
  <div class="photo" role="img" aria-label="Photo of an office worker at a desk with a monkey on his back"></div>
  <p class="q">When your employees talk to you,<br>what do they do?</p>
  <div class="dots" style="left:134px;top:82px"><i></i><i></i><i></i></div>
  <p class="b" style="top:91px">Leave monkeys on your back?</p>
  <p class="b" style="top:108px">Add monkeys to your back?</p>
  <p class="b" style="top:125px">Take monkeys off your back?</p>
  <div class="mark"><b></b>Bildmarkt</div>
  <div class="foot-line" style="background:var(--red)"></div>
</section>

<!-- Motivation matrix -->
<section class="slide matrix">
  <div class="side"><span class="h">Motivation Matrix</span></div>
  <svg width="299" height="168" style="position:absolute;left:0;top:0">
    <defs><marker id="mx" markerWidth="6" markerHeight="6" refX="5" refY="3" orient="auto"><path d="M0,0 L6,3 L0,6z" fill="#000"/></marker></defs>
    <line x1="165" y1="148" x2="165" y2="18" stroke="#000" stroke-width="2" marker-end="url(#mx)" marker-start="url(#mx)"/>
    <line x1="80" y1="80" x2="250" y2="80" stroke="#000" stroke-width="2" marker-end="url(#mx)"/>
    <line x1="250" y1="80" x2="80" y2="80" stroke="#000" stroke-width="2" marker-end="url(#mx)"/>
  </svg>
  <div class="ax" style="left:0;right:0;top:7px;padding-left:27px;margin-left:-30px">HIGH EFFORT</div>
  <div class="ax" style="left:0;right:0;bottom:2px;margin-left:-30px">LOW EFFORT</div>
  <div class="ax" style="left:33px;top:69px">LOW<br>AGREEMENT</div>
  <div class="ax" style="left:250px;top:75px">HIGH<br>AGREEMENT</div>
  <div class="q" style="left:84px;top:36px">CONCESSION<small>RIDING ALONG</small></div>
  <div class="q" style="left:178px;top:36px">BUY-IN<small>HIGHLY ENGAGED</small></div>
  <div class="q" style="left:84px;top:94px">RESENTMENT<small>HIGHLY DISENGAGED</small></div>
  <div class="q" style="left:178px;top:94px">EXEMPT<small>RIDING ALONG</small></div>
  <div class="mark"><b></b>Bildmarkt</div>
</section>

<!-- Magic circle -->
<section class="slide magic">
  <div class="wash"></div>
  <div class="bar-head red h">The Magic Circle</div>
  <svg width="299" height="168" style="position:absolute;left:0;top:0">
    <circle cx="150" cy="92" r="41" fill="#8d8d8d"/>
    <circle cx="150" cy="92" r="27" fill="#b4b4b4"/>
    <circle cx="150" cy="92" r="13" fill="#e6e6e6"/>
    <path d="M155 72 A20 20 0 0 1 155 112" fill="none" stroke="#b0272d" stroke-width="2.5"/>
    <path d="M62 84 H125 V80 L134 89 L125 98 V94 H62 Z" fill="#14307a"/>
    <path d="M168 84 H238 V80 L248 89 L238 98 V94 H168 Z" fill="#b0272d"/>
    <g font-family="Open Sans" fill="#fff" font-size="7" text-anchor="middle">
      <text x="150" y="63" font-weight="600">WHAT</text>
      <text x="150" y="77" fill="#14307a" font-weight="600">HOW</text>
      <text x="150" y="94" fill="#e8a21d" font-weight="700">WHY</text>
      <text x="94" y="92">TRADITIONAL</text>
      <text x="205" y="92">REMARKABLE</text>
    </g>
  </svg>
  <div class="credit">“MAGIC CIRCLE” CONCEPT COURTESY OF MARTEN VALE</div>
  <div class="mark"><b></b>Bildmarkt</div>
  <div class="foot-line" style="background:var(--red)"></div>
</section>

<!-- Driving the right culture -->
<section class="slide culture">
  <div class="photo" role="img" aria-label="Photo of a wheel loader and dump truck in a quarry"></div>
  <div class="panel"></div>
  <div class="t h">Driving<br>the<br>right<br>culture</div>
  <div class="dots"><i></i><i></i><i></i></div>
  <div class="mark"><b></b>Bildmarkt</div>
</section>

<p class="caption">Master slides with all slides includes - Easy / Quick Editable</p>

</body>
</html>
```